Mirrorglow 90's Revival club night

I am after either an A5 or DL flyer but also the formats for using the design on social media etc.
The flyer is for a 90's revival club night at a nightclub that was well attended in the 90's . A special guest PA - Honey Q famous for her single 'Carry me through the starlight' ,is performing.
I have a logo for the night that may have to be altered / edited to fit in with your design (Colours changed etc) but also have a logo for the artist that may be more restrictive in regards to any changes.Both are attached.
Look forward to hearing from you shortly,

Tam

Reason: Required text to go on the flyer has now be added to the brief. Majority of designs submitted didn't seem to reflect to '90's nightclub' feel we were hoping for. Most of the designs used the colour scheme based on the 'Mirrorglow' logo. We are hoping that these colours can be ignored with some designs and that the logo is made of of different colours that would make it easier for it to fit in with the designers ideas. Regards Tam

Target Market(s)

20 to 50 years age range who use to go clubbing / still do / love the 90's music. Club that they use to attend in the 90's is where the event is being held

Industry/Entity Type

Club

Requirements
Must have
• Both the logos for the event ( Mirrorglow 90's Revival and Honey Q ) must be included on the flyer. Colours and the format can be altered on the mirrorglow logo but the design should remain as close to the original as sent. 90's font and images would also be a must if possible. Honey Q logo can have colors altered, but not the font or design.
• Text required as follows :
• Venue : Club Orbit, Pellingford Lane, Westbury, Wiltshire
• Date : Saturday 10th June 2017
• Time : 8.30pm till 3am
• Very special guest PA ‘ HONEY Q’ ‘Carry me through the starlight’
• DJ’s : Main room – Danny Holtsby ( Arcade 77 / Mirrorglow )
• Room 2 – Simon P
• Full club décor with Laser lightshow, CO’2 cannons and pryrotechnics
• Tickets : £15 VIP / £10 General Admission – Available from : https://www.passgate-example.co.uk/venue/QZTRWN
• Or ‘Club Orbit’ : 01632 960418
• Web : www.ravebackclub-example.co.uk
Nice to have
• open to ideas
Should not have
• Not to cheesy ........

```html
<!DOCTYPE html>
<html lang="en">
<head>
<meta charset="utf-8">
<title>Mirrorglow 90's Revival – Honey Q flyer</title>
<link rel="stylesheet" href="https://fonts.googleapis.com/css2?family=Oswald:wght@500;600;700&family=Orbitron:wght@800;900&family=Yellowtail&family=Varela+Round&family=Lato:wght@400;700&display=swap">
<style>
  :root {
    --page-bg: #6b6b5e;
    --sky-top: #eef3fb;
    --sky-mid: #9fb2ea;
    --sky-low: #b7a6ea;
    --navy: #14246b;
    --blue: #1f5fc4;
    --royal: #1d43a6;
    --yellow: #f7e41a;
    --gold: #f4c400;
    --pink: #ff2fc8;
    --white: #ffffff;
    --ink: #222222;
  }
  * { margin: 0; padding: 0; box-sizing: border-box; }
  html, body { width: 771px; height: 1200px; overflow: hidden; }
  body { background: var(--page-bg); position: relative; }

  .flyer {
    position: absolute; left: 85px; top: 0; width: 600px; height: 1200px; overflow: hidden;
    background:
      radial-gradient(ellipse 300px 420px at 400px 420px, rgba(255,255,255,.75), rgba(255,255,255,0) 70%),
      linear-gradient(180deg, var(--sky-top) 0%, #c6d3f3 28%, var(--sky-mid) 55%, var(--sky-low) 78%, #9a8fd6 100%);
  }

  .event-badge {
    position: absolute; left: 295px; top: 52px; width: 256px; height: 256px; border-radius: 50%;
    background: radial-gradient(circle at 50% 40%, #d6e2f6, #8fa8de);
    border: 9px solid var(--yellow);
    display: flex; flex-direction: column; align-items: center; justify-content: center;
  }
  .event-badge__name {
    font-family: 'Oswald', sans-serif; font-weight: 600; color: var(--royal);
    font-size: 38px; line-height: 1.05; text-align: center;
  }

  .guest-photo {
    position: absolute; left: 13px; top: 120px; width: 275px; height: 460px;
    border-radius: 140px 140px 40px 20px;
    background: linear-gradient(170deg, #2c3f9c 0%, #3d4fa8 28%, #d9a995 45%, #eac3b2 70%, rgba(200,190,235,0) 100%);
  }

  .headline {
    position: absolute; right: 45px; font-family: 'Varela Round', sans-serif; color: var(--white);
    -webkit-text-stroke: 3px var(--royal); paint-order: stroke fill; line-height: 1;
  }
  .headline--special { top: 370px; font-size: 66px; letter-spacing: 1px; }
  .headline--guest { top: 452px; font-size: 84px; font-weight: 700; -webkit-text-stroke: 5px var(--royal); }

  .artist-name {
    position: absolute; left: 52px; top: 578px; width: 510px; text-align: center;
    font-family: 'Orbitron', sans-serif; font-weight: 900; font-size: 44px; color: var(--yellow);
    -webkit-text-stroke: 5px var(--ink); paint-order: stroke fill; letter-spacing: 2px;
    transform: skewX(-10deg);
  }

  .single-title {
    position: absolute; left: 120px; top: 630px; width: 470px; text-align: center;
    font-family: 'Yellowtail', cursive; color: #fff4fd; font-size: 62px; line-height: 1.3;
    -webkit-text-stroke: 2px var(--pink); paint-order: stroke fill;
    text-shadow: 0 0 10px rgba(255,47,200,.7);
  }

  .time-badge {
    position: absolute; left: 38px; top: 758px; width: 182px; height: 182px; border-radius: 50%;
    background: var(--white); border: 6px solid var(--royal);
    box-shadow: -5px -4px 0 4px var(--yellow);
    display: flex; flex-direction: column; align-items: center; justify-content: center;
    font-family: 'Oswald', sans-serif; font-weight: 600; line-height: 1.1;
  }
  .time-badge__start { color: var(--blue); font-size: 40px; }
  .time-badge__end { color: var(--navy); font-size: 40px; }

  .event-date {
    position: absolute; left: 232px; top: 846px; width: 330px; text-align: center;
    font-family: 'Oswald', sans-serif; font-weight: 600; font-size: 30px; color: var(--navy);
    text-shadow: 1px 1px 0 var(--yellow), -1px -1px 0 var(--yellow), 1px -1px 0 var(--yellow), -1px 1px 0 var(--yellow);
  }

  .ticket-prices { position: absolute; left: 234px; top: 897px; height: 36px; display: flex; font-family: 'Oswald', sans-serif; }
  .ticket-prices__vip { width: 131px; background: var(--white); color: var(--ink); font-weight: 700; font-size: 27px; text-align: center; line-height: 36px; }
  .ticket-prices__general { width: 194px; background: var(--royal); color: var(--yellow); font-weight: 600; font-size: 17px; text-align: center; line-height: 36px; border-right: 3px solid var(--white); }

  .ticket-source { position: absolute; left: 230px; top: 942px; width: 336px; text-align: center; font-family: 'Lato', sans-serif; }
  .ticket-source__label { color: var(--royal); font-weight: 700; font-size: 19px; }
  .ticket-source__url { color: var(--ink); font-size: 12.5px; margin-top: 2px; }

  .dj-lineup { position: absolute; left: 228px; top: 994px; width: 345px; text-align: center; font-family: 'Oswald', sans-serif; font-weight: 500; font-size: 13.5px; color: var(--white); line-height: 1.55; }
  .dj-lineup__room2 { color: var(--pink); }

  .club-features { position: absolute; left: 20px; top: 963px; width: 220px; text-align: center; font-family: 'Lato', sans-serif; font-size: 13px; color: var(--ink); line-height: 1.35; }
  .club-phone { position: absolute; left: 20px; top: 1023px; width: 220px; text-align: center; font-family: 'Oswald', sans-serif; font-weight: 600; font-size: 15px; color: var(--yellow); -webkit-text-stroke: 2px var(--ink); paint-order: stroke fill; }

  .footer-band { position: absolute; left: 0; top: 1035px; width: 600px; height: 165px; }
  .artist-mark { position: absolute; left: 0; top: 1080px; width: 600px; text-align: center; font-family: 'Oswald', sans-serif; font-weight: 600; font-size: 40px; color: var(--ink); }
  .web-address { position: absolute; left: 0; top: 1142px; width: 600px; text-align: center; font-family: 'Lato', sans-serif; font-size: 15px; letter-spacing: 3px; color: var(--ink); }
</style>
</head>
<body>
  <main class="flyer">
    <div class="event-badge">
      <div class="event-badge__name">Mirrorglow<br>90's Revival</div>
    </div>

    <div class="guest-photo" role="img" aria-label="Photo of the female guest vocalist with sleek blue hair holding a microphone"></div>

    <div class="headline headline--special">SPECIAL</div>
    <div class="headline headline--guest">GUEST</div>

    <div class="artist-name">PA-HONEY Q</div>
    <div class="single-title">Carry me through<br>the starlight</div>

    <div class="time-badge">
      <span class="time-badge__start">8.30pm</span>
      <span class="time-badge__end">till 3am</span>
    </div>

    <div class="event-date">Saturday 10th June 2017</div>

    <div class="ticket-prices">
      <div class="ticket-prices__vip">£15 VIP</div>
      <div class="ticket-prices__general">£10 General Admission</div>
    </div>

    <div class="ticket-source">
      <div class="ticket-source__label">Available from :</div>
      <div class="ticket-source__url">https://www.passgate-example.co.uk/venue/QZTRWN</div>
    </div>

    <div class="dj-lineup">
      DJ's : Main room – Danny Holtsby ( Arcade 77 / Mirrorglow<br>
      <span class="dj-lineup__room2">Room 2 – Simon P</span>
    </div>

    <div class="club-features">Full club décor with Laser lightshow, CO'2 cannons and pryrotechnics</div>
    <div class="club-phone">Club Orbit' : 01632 960418</div>

    <svg class="footer-band" viewBox="0 0 600 165" aria-hidden="true">
      <defs>
        <linearGradient id="bandYellow" x1="0" y1="0" x2="0" y2="1">
          <stop offset="0" stop-color="#f9ea2a"/>
          <stop offset="1" stop-color="#f3c300"/>
        </linearGradient>
      </defs>
      <path d="M0 60 Q300 -30 600 60 V165 H0 Z" fill="#ffffff"/>
      <path d="M0 80 Q300 -8 600 80 V165 H0 Z" fill="url(#bandYellow)"/>
    </svg>
    <div class="artist-mark">Honey Q</div>
    <div class="web-address">www.ravebackclub-example.co.uk</div>
  </main>
</body>
</html>
```